WP website design (Brisden)

We need a wordpress design for an established auction and real estate company based in Kentucky. The winning design will incorporate a professional color scheme with company logo in a clean layout with specified widgets. The design needs to consider that this will be developed on a responsive theme. Color is #307d84, with gray/black or other as an accent/highlight color.

Industry/Entity Type

Real Estate

Requirements
Must have
• Elelments of design need to consider that this site is going to be developed on a responsive theme.

Navigation:
1) Home 2) Current Auctions 3) Past Auctions 4) Meet the Staff 5) For Sellers 6) For Buyers 7) Testimonials 8) Contact Us

Colors will be the blue of logo plus black/gray or other accent color.

Slideshow will be prominent, please use stock real estate photo for initial image. Will have following in either header or sidebar: testimonials, social icons (FB, linkedin Twitter, RSS), Featured Auctions widget, newsletter signup form.

Footer will have contact info (below) and attached affiliation logos.
Brisden Auctions, Inc.
48710 Pomeroy Rd., Louisville KY 40199
dan.office@brisdenbid.example
Phone: (502) 555 0172

```html
<!DOCTYPE html>
<html lang="en">
<head>
<meta charset="utf-8">
<title>Brisden Auctions, Inc.</title>
<link href="https://fonts.googleapis.com/css2?family=Raleway:wght@400;500;600;700;800&family=Open+Sans:wght@400;600;700&display=swap" rel="stylesheet">
<style>
:root{
  --teal:#1b8884;
  --teal-dark:#136f6b;
  --orange:#f8b545;
  --orange-dark:#e79e25;
  --dark:#2f2f2f;
  --darker:#232323;
  --text:#555;
  --muted:#888;
  --line:#d8d8d8;
  --bg:#fff;
}
*{box-sizing:border-box;margin:0;padding:0}
html,body{width:1200px;height:2644px;overflow:hidden;background:var(--bg)}
body{font-family:"Open Sans",sans-serif;color:var(--text);font-size:12px;position:relative}
a{color:inherit;text-decoration:none}
.wrap{position:absolute;left:79px;width:1042px}

/* top bar */
.topbar{position:absolute;top:0;left:0;width:1200px;height:28px;border-bottom:1px solid var(--line)}
.topbar .welcome{position:absolute;left:79px;top:7px;font-size:11px;color:var(--muted)}
.topbar .welcome a{color:var(--teal)}
.topbar .account{position:absolute;left:914px;top:0;width:44px;height:28px;border-left:1px solid var(--line);border-right:1px solid var(--line)}
.topbar .search{position:absolute;left:958px;top:0;width:163px;height:28px;border-right:1px solid var(--line);font-size:11px;color:#aaa;padding:7px 10px}
.topbar svg{position:absolute}

/* header */
.header{top:40px;height:66px}
.phone-line{position:absolute;left:0;top:24px;font-size:11px;color:var(--dark)}
.phone-line span{color:var(--teal)}
.brand{position:absolute;left:450px;top:10px;display:flex;align-items:center;gap:8px}
.brand-mark{width:20px;height:20px;background:var(--orange)}
.brand-name{font-family:"Raleway",sans-serif;font-weight:800;font-size:22px;line-height:1;color:var(--teal)}
.social{position:absolute;right:0;top:18px;display:flex;gap:9px}
.social span{width:26px;height:26px;border-radius:50%;background:var(--dark)}
.social span:first-child{background:#3b5a9a}

/* nav */
.nav{top:114px;height:44px;border:1px solid var(--line);display:flex;justify-content:center;gap:0}
.nav a{font-family:"Raleway",sans-serif;font-weight:700;font-size:11px;color:var(--dark);letter-spacing:.5px;padding:0 13px;line-height:42px;position:relative}
.nav a.active,.nav a.open{color:var(--teal)}
.nav a.active::before,.nav a.open::before{content:"";position:absolute;left:0;right:0;top:-1px;height:3px;background:var(--teal)}
.dropdown{position:absolute;left:385px;top:158px;width:203px;background:#fff;box-shadow:0 2px 6px rgba(0,0,0,.18);z-index:5}
.dropdown a{display:block;font-size:11px;color:var(--muted);padding:0 17px;line-height:31px;border-bottom:1px solid #eee}
.dropdown a.hover{color:var(--teal)}

/* slider */
.slider{top:177px;height:555px;background:linear-gradient(180deg,#8db5e0 0%,#b9d2ec 30%,#9c8f7c 55%,#6f7a52 80%,#4d6b2e 100%)}
.arrow{position:absolute;width:22px;height:40px;background:rgba(0,0,0,.25)}
.slider .arrow.l{left:0;top:254px}
.slider .arrow.r{right:0;top:254px}
.dots{position:absolute;left:500px;bottom:14px;display:flex;gap:3px}
.dots i{width:10px;height:10px;border:1px solid #fff;background:rgba(255,255,255,.3)}
.dots i:first-child{background:var(--teal)}

/* section headings */
.sec-title{position:absolute;left:79px;width:1042px;height:20px}
.sec-title::before{content:"";position:absolute;left:0;right:0;top:10px;height:1px;background:var(--line)}
.sec-title span{position:absolute;left:50%;transform:translateX(-50%);top:0;background:#fff;border:2px solid var(--line);font-family:"Raleway",sans-serif;font-weight:700;font-size:11px;letter-spacing:1.5px;color:var(--dark);padding:3px 26px}

/* auction cards */
.cards{top:820px;height:545px;display:flex;gap:27px}
.card{width:240px;position:relative}
.card-box{border:1px solid var(--line);height:502px}
.card-photo{height:343px}
.p1{background:linear-gradient(180deg,#5a8bd0,#9c8b70 55%,#6f8a4a)}
.p2{background:linear-gradient(180deg,#7fb0e6,#7b9a8a 50%,#5b7a45)}
.p3{background:linear-gradient(180deg,#3f7bd6,#c7a978 55%,#6d8f44)}
.p4{background:linear-gradient(180deg,#8fb7e1,#9b5b3e 50%,#7a6e5a)}
.card-info{padding:18px 10px 0;font-size:10px}
.row{display:flex;margin-bottom:10px;line-height:1.45}
.row b{font-weight:400;color:var(--dark);width:80px;flex:none}
.row span{color:var(--muted)}
.learn{display:block;text-align:center;font-size:10px;color:var(--teal);margin-top:4px}
.bid{display:block;margin:14px auto 0;width:112px;height:28px;border:2px solid var(--line);background:#fff;font-family:"Raleway",sans-serif;font-weight:700;font-size:10px;color:var(--dark);letter-spacing:.5px;text-align:center;line-height:24px}
.bid.on{background:var(--teal);border-color:var(--teal-dark);color:#fff}
.card .arrow{width:18px;height:40px;background:var(--teal);top:150px}
.card .arrow.l{left:0}.card .arrow.r{right:0}

/* widgets */
.panel{position:absolute;overflow:hidden}
.auctions{left:79px;top:1400px;width:330px;height:416px;background:var(--dark);padding:16px 18px}
.tabs{display:flex;font-family:"Raleway",sans-serif;font-size:12px;font-weight:600}
.tabs span{flex:1;text-align:center;line-height:28px;color:#fff;background:#444}
.tabs span.on{background:var(--teal)}
.schedule{text-align:center;color:#fff;font-size:11px;margin:8px 0 6px}
.list{background:#fff;height:314px;position:relative;overflow:hidden}
.list .scroll{position:absolute;right:2px;top:2px;width:9px;height:310px;background:#ddd}
.list .scroll i{display:block;height:200px;background:#aaa}
.item{display:flex;gap:8px;padding:8px 16px 8px 4px;border-bottom:4px solid var(--dark);height:120px}
.thumb{width:88px;height:82px;flex:none;background:linear-gradient(180deg,#7fa8d8,#a58b6a 55%,#6d8a48)}
.item h4{font-family:"Open Sans",sans-serif;font-size:12px;color:var(--dark);line-height:1.35}
.item h4 em{font-weight:400;font-size:10px;color:var(--muted)}
.item ul{list-style:none;font-size:11px;color:var(--dark);margin-top:10px}
.item li{line-height:20px}
.item li::before{content:"";display:inline-block;border-left:5px solid var(--dark);border-top:4px solid transparent;border-bottom:4px solid transparent;margin-right:6px}

.newsletter{left:433px;top:1400px;width:509px;height:191px;background:var(--teal);color:#fff;padding:16px 22px}
.newsletter h3{font-family:"Raleway",sans-serif;font-weight:700;font-size:23px;display:flex;align-items:center;gap:8px}
.newsletter p{font-size:12px;line-height:1.55;margin:14px 0 12px}
.form{display:flex;height:42px}
.form .input{flex:1;background:#fff;color:var(--muted);font-size:12px;padding:12px 14px}
.form .btn{width:96px;background:var(--orange);font-family:"Raleway",sans-serif;font-weight:700;font-size:12px;line-height:42px;text-align:center}

.brochure{left:968px;top:1400px;width:153px;height:191px;background:var(--orange);text-align:center;padding-top:16px}
.brochure h3{font-family:"Raleway",sans-serif;font-weight:700;font-size:22px;color:#fff;line-height:1.05}
.brochure .doc{display:block;margin:10px auto 6px}
.brochure .dl{display:block;margin:0 auto;width:72px;height:36px;background:var(--dark)}

.trust{left:433px;top:1613px;width:334px;height:203px;background:var(--orange);padding:16px 18px;display:flex;gap:14px}
.trust h3{font-family:"Raleway",sans-serif;font-weight:700;font-size:22px;color:#fff;line-height:1.15;width:120px}
.trust p{font-size:11px;color:var(--dark);line-height:1.45;margin-top:12px;width:120px}
.trust .actions h5{font-family:"Raleway",sans-serif;font-weight:700;font-size:13px;color:#fff;letter-spacing:.5px;margin-bottom:7px}
.trust .actions a{display:flex;justify-content:space-between;align-items:center;background:var(--dark);color:#fff;font-size:12px;padding:0 10px;height:30px;width:170px;margin-bottom:10px}
.trust .actions a::after{content:"";border-left:5px solid #fff;border-top:4px solid transparent;border-bottom:4px solid transparent}
.trust .actions h5.second{margin-top:6px}

.testimonials{left:792px;top:1613px;width:329px;height:203px;background:var(--dark);color:#fff}
.testimonials h3{font-family:"Raleway",sans-serif;font-weight:700;font-size:20px;padding:10px 18px;height:46px;border-bottom:1px solid #444;display:flex;justify-content:space-between;align-items:center}
.nav-dots{display:flex;gap:5px}
.nav-dots i{width:15px;height:15px;border-radius:50%;background:#fff}
.quote{display:flex;gap:16px;padding:16px 18px 0}
.avatar{width:62px;height:62px;flex:none;background:linear-gradient(180deg,#c9b8a4,#6f5c4a)}
.quote p{font-size:11px;line-height:1.6;color:#ddd}
.quote .who{font-size:11px;line-height:1.5;margin-top:12px;color:#fff}
.quote .who b{display:block}
.quote .who span{color:#ccc}

/* team */
.team{top:1851px;height:293px;background:var(--teal)}
.team .sec-label{position:absolute;left:0;right:0;top:36px;height:1px;background:rgba(255,255,255,.6)}
.team .sec-label span{position:absolute;left:50%;transform:translateX(-50%);top:-11px;background:var(--teal);border:2px solid rgba(255,255,255,.8);font-family:"Raleway",sans-serif;font-weight:700;font-size:11px;letter-spacing:1.5px;color:#fff;padding:3px 24px}
.members{position:absolute;left:96px;top:90px;display:flex;gap:35px}
.member{width:142px;text-align:center}
.member .photo{height:142px;border:2px solid #fff;background:linear-gradient(180deg,#4a4a4a,#8d7a6a)}
.member p{color:#fff;font-size:12px;margin-top:14px}
.team .arrow{width:18px;height:40px;background:rgba(255,255,255,.25);border:1px solid #fff;top:148px}
.team .arrow.l{left:0}.team .arrow.r{right:0}

/* affiliations */
.affil{top:2225px;height:124px;border:1px solid var(--line);display:flex;justify-content:space-around;align-items:center;padding:0 60px}
.badge{background:#c8c8c8}

/* footer */
.footer{position:absolute;left:79px;top:2370px;width:1042px;height:230px;background:var(--darker);display:flex;padding:26px 22px;gap:44px}
.fcol{width:224px}
.fcol h4{font-family:"Raleway",sans-serif;font-weight:700;font-size:13px;color:#fff;letter-spacing:.5px;margin-bottom:16px}
.fcol p{font-size:11px;line-height:1.6;color:#ccc}
.fcol ul{list-style:none}
.fcol li{font-size:11px;color:#ccc;line-height:31px}
.contact li{display:flex;gap:14px;align-items:flex-start;line-height:1.5;margin-bottom:18px}
.contact svg{flex:none}
.copy{position:absolute;left:79px;top:2600px;width:1042px;height:44px;background:#111;color:#aaa;font-size:11px;padding:14px 22px}
</style>
</head>
<body>

<div class="topbar">
  <div class="welcome">Welcome visitor you can <a href="#">login</a> or <a href="#">create an account</a></div>
  <div class="account"><svg width="44" height="28" viewBox="0 0 44 28"><circle cx="17" cy="11" r="3" fill="#555"/><path d="M12 19c0-3 2-4.5 5-4.5s5 1.5 5 4.5z" fill="#555"/><path d="M26 13l3 3 3-3z" fill="#555"/></svg></div>
  <div class="search">Search...<svg width="12" height="12" viewBox="0 0 12 12" style="right:10px;top:8px"><circle cx="5" cy="5" r="3.6" stroke="#555" stroke-width="1.6" fill="none"/><path d="M7.6 7.6L11 11" stroke="#555" stroke-width="1.8"/></svg></div>
</div>

<header class="wrap header">
  <div class="phone-line"><svg width="10" height="10" viewBox="0 0 10 10"><path d="M2 0l2 2.5-1.2 1.3c.6 1.4 1.6 2.4 3 3L7 5.6 9.5 7.6 8.3 9.6C4 9 1 6 .4 1.7z" fill="#333"/></svg>&nbsp; Call Us: <span>(502) 555 0172</span></div>
  <div class="brand"><i class="brand-mark"></i><span class="brand-name">Brisden Auctions inc.</span></div>
  <div class="social" aria-label="Social links"><span></span><span></span><span></span><span></span></div>
</header>

<nav class="wrap nav">
  <a class="active" href="#">HOME</a>
  <a href="#">CURRENT AUCTIONS</a>
  <a class="open" href="#">PAST AUCTIONS</a>
  <a href="#">MEET THE STAFF</a>
  <a href="#">FOR SELLERS</a>
  <a href="#">FOR BUYERS</a>
  <a href="#">TESTIMONIALS</a>
  <a href="#">CONTACT US</a>
</nav>
<div class="dropdown">
  <a href="#">Lorem Ipsum Dolor</a>
  <a class="hover" href="#">Lorem Ipsum Dolor</a>
  <a href="#">Lorem Ipsum Dolor</a>
  <a href="#">Lorem Ipsum Dolor</a>
</div>

<section class="wrap slider" role="img" aria-label="Slideshow photo of a large two-storey family home with front porch and lawn at dusk">
  <span class="arrow l"></span><span class="arrow r"></span>
  <div class="dots"><i></i><i></i><i></i></div>
</section>

<div class="sec-title" style="top:767px"><span>CURRENT AUCTIONS</span></div>

<section class="wrap cards">
  <article class="card">
    <div class="card-box">
      <div class="card-photo p1" role="img" aria-label="Photo of a stone and shingle house with curved driveway"></div>
      <div class="card-info">
        <div class="row"><b>Description:</b><span>Lorem ipsum dolor sit amet, consectetuer adipiscing elit.</span></div>
        <div class="row"><b>Address:</b><span>Linden Valley/ Maple Hill area</span></div>
        <div class="row"><b>Bidding Ends:</b><span>Thursday, July 10, 2014</span></div>
        <a class="learn" href="#">Learn more ▸</a>
      </div>
    </div>
    <a class="bid on" href="#">CLICK TO BID</a>
    <span class="arrow l"></span>
  </article>
  <article class="card">
    <div class="card-box">
      <div class="card-photo p2" role="img" aria-label="Photo of a green two-storey house with porch"></div>
      <div class="card-info">
        <div class="row"><b>Description:</b><span>Lorem ipsum dolor sit amet, consectetuer adipiscing elit.</span></div>
        <div class="row"><b>Address:</b><span>7710 Oakmere Rd, Louisville, KY 40219</span></div>
        <div class="row"><b>Bidding Ends:</b><span>Thursday, July 17, 2014</span></div>
        <a class="learn" href="#">Learn more ▸</a>
      </div>
    </div>
    <a class="bid" href="#">CLICK TO BID</a>
  </article>
  <article class="card">
    <div class="card-box">
      <div class="card-photo p3" role="img" aria-label="Photo of a beige stucco house under blue sky"></div>
      <div class="card-info">
        <div class="row"><b>Description:</b><span>Lorem ipsum dolor sit amet, consectetuer adipiscing elit.</span></div>
        <div class="row"><b>Address:</b><span>Hwy 19 in Elmridge/ Fox Hollow area</span></div>
        <div class="row"><b>Bidding Ends:</b><span>Thursday, July 28, 2014</span></div>
        <a class="learn" href="#">Learn more ▸</a>
      </div>
    </div>
    <a class="bid" href="#">CLICK TO BID</a>
  </article>
  <article class="card">
    <div class="card-box">
      <div class="card-photo p4" role="img" aria-label="Photo of a red brick house with white windows"></div>
      <div class="card-info">
        <div class="row"><b>Description:</b><span>Lorem ipsum dolor sit amet, consectetuer adipiscing elit.</span></div>
        <div class="row"><b>Address:</b><span>3380 Harlow Industrial Blvd., Louisville, KY 40288</span></div>
        <div class="row"><b>Bidding Ends:</b><span>Thursday, July 30, 2014</span></div>
        <a class="learn" href="#">Learn more ▸</a>
      </div>
    </div>
    <a class="bid" href="#">CLICK TO BID</a>
    <span class="arrow r"></span>
  </article>
</section>

<section class="panel auctions">
  <div class="tabs"><span class="on">Open Auctions</span><span>Closed Auctions</span></div>
  <div class="schedule">▦ View Full Auction Schedule</div>
  <div class="list">
    <div class="item"><div class="thumb" role="img" aria-label="Photo of a duplex house"></div><div><h4>2014 July 07-10 Suburban Duplex Auction <em>Ends Jul 10</em></h4><ul><li>Auction Home</li><li>View Lots</li></ul></div></div>
    <div class="item"><div class="thumb" role="img" aria-label="Photo of a summer house"></div><div><h4>2014 July 15-17 Summer House Auction <em>Ends Jul 17</em></h4><ul><li>Auction Home</li><li>View Lots</li></ul></div></div>
    <div class="item"><div class="thumb" role="img" aria-label="Photo of a red brick house"></div><div><h4>2014 Aug 02-06 Red Brick House Auction <em>Ends Aug 06</em></h4></div></div>
    <div class="scroll"><i></i></div>
  </div>
</section>

<section class="panel newsletter">
  <h3><svg width="20" height="16" viewBox="0 0 20 16"><rect x="1" y="1" width="18" height="14" fill="none" stroke="#fff" stroke-width="2"/><path d="M1 2l9 7 9-7" fill="none" stroke="#fff" stroke-width="2"/></svg>Newsletter Signup</h3>
  <p>Sign up for our weekly email newsletter to receive updates about market stats, buyer and seller articles and latest auctions.</p>
  <div class="form"><div class="input">Enter your email address...</div><div class="btn">Subscribe</div></div>
</section>

<section class="panel brochure">
  <h3>Download<br>Brochure</h3>
  <svg class="doc" width="30" height="36" viewBox="0 0 30 36"><path d="M2 1h18l8 8v26H2z" fill="#fff" stroke="#ccc"/><rect x="0" y="14" width="22" height="10" fill="#d9362b"/></svg>
  <span class="dl"><svg width="72" height="36" viewBox="0 0 72 36"><path d="M36 9v12M31 16l5 5 5-5M28 25h16" stroke="#fff" stroke-width="2.4" fill="none"/></svg></span>
</section>

<section class="panel trust">
  <div>
    <h3>Trust The Experts. Sell With The Best.</h3>
    <p>Get started with free research and valuation</p>
  </div>
  <div class="actions">
    <h5>VALUE YOUR ITEM</h5>
    <a href="#">Search Archives</a>
    <a href="#">View Value Guides</a>
    <h5 class="second">SELL YOUR ITEM</h5>
    <a href="#">Contact A Specialist</a>
  </div>
</section>

<section class="panel testimonials">
  <h3>Testimonials<span class="nav-dots"><i></i><i></i></span></h3>
  <div class="quote">
    <div class="avatar" role="img" aria-label="Portrait of the client"></div>
    <div>
      <p>Typi non habent claritatem insitam; est usus legentis in iis qui facit eorum clari atem qui nunc nobis videntur parum clari, fiant sollemnes in futurum.</p>
      <div class="who"><b>Martin Coles</b><span>Owner, Company</span></div>
    </div>
  </div>
</section>

<section class="wrap team">
  <div class="sec-label"><span>MEET THE TEAM</span></div>
  <div class="members">
    <div class="member"><div class="photo" role="img" aria-label="Portrait of Dan Brisden"></div><p>Dan Brisden</p></div>
    <div class="member"><div class="photo" role="img" aria-label="Portrait of Joe Haskell"></div><p>Joe Haskell</p></div>
    <div class="member"><div class="photo" role="img" aria-label="Portrait of Allee Marston"></div><p>Allee Marston</p></div>
    <div class="member"><div class="photo" role="img" aria-label="Portrait of Bill Trevane"></div><p>Bill Trevane</p></div>
    <div class="member"><div class="photo" role="img" aria-label="Portrait of Caitlin Brisden Pryor"></div><p>Caitlin Brisden Pryor</p></div>
  </div>
  <span class="arrow l"></span><span class="arrow r"></span>
</section>

<div class="sec-title" style="top:2179px"><span>AFFILIATIONS</span></div>

<section class="wrap affil" aria-label="Affiliation badges">
  <span class="badge" style="width:130px;height:60px;border-radius:30px"></span>
  <span class="badge" style="width:64px;height:72px"></span>
  <span class="badge" style="width:48px;height:78px"></span>
  <span class="badge" style="width:68px;height:70px"></span>
  <span class="badge" style="width:60px;height:70px"></span>
</section>

<footer class="footer">
  <div class="fcol">
    <h4>ABOUT US</h4>
    <p>Brisden Auctions Inc. is a full time auction company engaged in the marketing and sale of real estate and personal property by auction. The auctioneers with Brisden Auctions are licensed to do business in the States of Kentucky, and Indiana.</p>
  </div>
  <div class="fcol">
    <h4>INFORMATION</h4>
    <ul><li>Current Auctions</li><li>Past Auctions</li><li>For Sellers</li><li>For Buyers</li><li>Testimonials</li></ul>
  </div>
  <div class="fcol">
    <h4>LINKS</h4>
    <ul><li>Newsletter</li><li>Classifieds</li><li>Download Brochure</li><li>Terms and Conditions</li><li>Privacy Policy</li></ul>
  </div>
  <div class="fcol contact">
    <h4>CONTACT US</h4>
    <ul>
      <li><svg width="22" height="22" viewBox="0 0 22 22"><circle cx="11" cy="11" r="10" fill="none" stroke="#ccc"/><path d="M11 5a4 4 0 00-4 4c0 3 4 8 4 8s4-5 4-8a4 4 0 00-4-4z" fill="#ccc"/><circle cx="11" cy="9" r="1.4" fill="#232323"/></svg><span>Brisden Auctions, Inc.<br>48710 Pomeroy Rd.,<br>Louisville KY 40199</span></li>
      <li><svg width="22" height="22" viewBox="0 0 22 22"><circle cx="11" cy="11" r="10" fill="none" stroke="#ccc"/><rect x="6" y="7.5" width="10" height="7" fill="none" stroke="#ccc"/><path d="M6 8l5 4 5-4" fill="none" stroke="#ccc"/></svg><span>dan.office@brisdenbid.example</span></li>
      <li><svg width="22" height="22" viewBox="0 0 22 22"><circle cx="11" cy="11" r="10" fill="none" stroke="#ccc"/><path d="M8 6l2 2.4-1 1.2c.5 1.2 1.4 2 2.6 2.6l1.1-1 2.3 1.8-1 1.8C10 14.4 7.6 12 7 8z" fill="#ccc"/></svg><span>(502) 555 0172</span></li>
    </ul>
  </div>
</footer>
<div class="copy">Copyright © 2014 BrisdenAuctions. All Rights Reserved.</div>

</body>
</html>
```